Painting Valtoni Renovations New buildings

Paint jobs plasterwork renovations new building customer painter paper drywall Entsorgungen.neukunden win color splash pleasure in colors competent clean fast reliable new try build demolition color combinations color concepts offers washing façade painting wood stains new projects old building renovations yes no beautiful new old sell secure solve paint over paint paint spray paint lye assemble disassemble sell buy trade oil dust new old assembly disassembly putty sanding fashion devastation copying belief feng shui kleopatra pompes beer colors swamp lime abrasion release tighten

Target Market(s)

construction industry

Contact Information for Business Card

Maler

Font styles to use
Serif

Colors
f04a50
959595

Requirements
Must have
• elegant appearance
Nice to have
• simply goal-oriented clientele in detail
Should not have
• too colorful

```html
<!DOCTYPE html>
<html lang="en">
<head>
<meta charset="utf-8">
<title>Corvano Malerbetrieb – Business Card</title>
<link rel="stylesheet" href="https://fonts.googleapis.com/css2?family=Merriweather:ital,wght@0,400;0,700;0,900;1,700&display=swap">
<style>
  :root {
    --stage: #e9e7e3;
    --card-white: #ffffff;
    --card-shade: #eef0f2;
    --brand-blue: #1f5ca3;
    --brand-blue-deep: #174a88;
    --ink-blue: #1c4f8f;
    --text-light: #ffffff;
    --rule-light: rgba(255,255,255,0.75);
    --r-red: #e8484f;
    --r-orange: #f39a2b;
    --r-yellow: #f2e52a;
    --r-green: #5cc24a;
    --r-cyan: #1fb6d8;
    --r-magenta: #c84fa8;
  }
  * { box-sizing: border-box; margin: 0; padding: 0; }
  html, body { width: 1200px; height: 780px; overflow: hidden; }
  body {
    background: var(--stage);
    font-family: "Merriweather", Georgia, serif;
    position: relative;
  }
  .card {
    position: absolute;
    top: 75px;
    width: 360px;
    height: 630px;
    border-radius: 18px;
    overflow: hidden;
    background: var(--card-white);
    box-shadow: 0 10px 30px rgba(0,0,0,0.18);
  }
  .card--front { left: 190px; }
  .card--back {
    left: 650px;
    background: linear-gradient(160deg, var(--card-white) 40%, var(--card-shade));
  }
  .card__art { position: absolute; inset: 0; }

  .brand {
    position: absolute;
    left: 0; right: 0;
    display: flex;
    flex-direction: column;
    align-items: center;
    color: var(--brand-blue);
  }
  .brand__row { display: flex; align-items: center; gap: 12px; }
  .brand__dot {
    width: 22px; height: 22px; border-radius: 50%;
    background: var(--brand-blue);
  }
  .brand__name { font-weight: 900; font-size: 44px; letter-spacing: 1px; }
  .brand__tag { font-weight: 400; font-size: 15px; letter-spacing: 3px; margin-top: 4px; }
  .card--front .brand { top: 100px; }
  .card--back .brand { top: 260px; }
  .card--back .brand__name { font-size: 54px; }
  .card--back .brand__dot { width: 28px; height: 28px; }

  .contact {
    position: absolute;
    left: 0; right: 0;
    top: 330px;
    color: var(--text-light);
    text-align: center;
  }
  .contact__name { font-weight: 700; font-size: 22px; }
  .contact__role { font-size: 14px; margin-top: 2px; }
  .contact__divider {
    display: flex; align-items: center; justify-content: center;
    gap: 10px; margin: 12px auto 8px; width: 270px;
  }
  .contact__divider::before, .contact__divider::after {
    content: ""; flex: 1; height: 1.5px; background: var(--rule-light);
  }
  .contact__icon {
    width: 30px; height: 30px; border-radius: 50%;
    background: var(--text-light);
    display: flex; align-items: center; justify-content: center;
  }
  .contact__phone { font-size: 19px; }
  .contact__address { font-size: 15px; line-height: 1.45; }

  .web {
    position: absolute;
    left: 0; right: 0; bottom: 16px;
    text-align: center;
    font-style: italic; font-weight: 700; font-size: 17px;
    color: var(--ink-blue);
  }
</style>
</head>
<body>

<section class="card card--front" aria-label="Business card front">
  <svg class="card__art" width="360" height="630" viewBox="0 0 360 630" aria-hidden="true">
    <defs>
      <linearGradient id="swoosh" x1="0" x2="1" y1="0" y2="0">
        <stop offset="0" stop-color="var(--r-orange)"/>
        <stop offset="0.35" stop-color="var(--r-yellow)"/>
        <stop offset="0.7" stop-color="var(--r-green)"/>
        <stop offset="1" stop-color="var(--brand-blue)"/>
      </linearGradient>
      <linearGradient id="panel" x1="0" x2="0" y1="0" y2="1">
        <stop offset="0" stop-color="var(--brand-blue)"/>
        <stop offset="1" stop-color="var(--brand-blue-deep)"/>
      </linearGradient>
      <linearGradient id="rainbow" x1="0" x2="1" y1="0" y2="0">
        <stop offset="0" stop-color="var(--r-red)"/>
        <stop offset="0.18" stop-color="var(--r-orange)"/>
        <stop offset="0.36" stop-color="var(--r-yellow)"/>
        <stop offset="0.54" stop-color="var(--r-green)"/>
        <stop offset="0.74" stop-color="var(--r-cyan)"/>
        <stop offset="1" stop-color="var(--r-magenta)"/>
      </linearGradient>
    </defs>
    <path d="M0 268 Q170 246 360 330 L360 566 L0 566 Z" fill="url(#panel)"/>
    <path d="M0 262 Q170 238 360 322" fill="none" stroke="url(#swoosh)" stroke-width="8"/>
    <path d="M70 288 Q230 280 360 352" fill="none" stroke="#ffffff" stroke-width="2" opacity="0.8"/>
    <rect x="0" y="566" width="360" height="6" fill="#ffffff"/>
    <rect x="0" y="572" width="360" height="58" fill="url(#rainbow)"/>
  </svg>

  <div class="brand">
    <div class="brand__row">
      <span class="brand__name">Corvano</span>
      <span class="brand__dot"></span>
    </div>
    <span class="brand__tag">Malerbetrieb</span>
  </div>

  <div class="contact">
    <p class="contact__name">Merenda Valtoni</p>
    <p class="contact__role">Manager</p>
    <div class="contact__divider">
      <span class="contact__icon">
        <svg width="16" height="16" viewBox="0 0 24 24" aria-label="Phone"><path d="M6.6 10.8a15 15 0 0 0 6.6 6.6l2.2-2.2c.3-.3.7-.4 1-.2 1.1.4 2.3.6 3.6.6.6 0 1 .4 1 1V20c0 .6-.4 1-1 1A17 17 0 0 1 3 4c0-.6.4-1 1-1h3.5c.6 0 1 .4 1 1 0 1.3.2 2.5.6 3.6.1.3 0 .7-.2 1z" fill="var(--brand-blue)"/></svg>
      </span>
    </div>
    <p class="contact__phone">(555) 210 4437</p>
    <div class="contact__divider">
      <span class="contact__icon">
        <svg width="16" height="16" viewBox="0 0 24 24" aria-label="Location"><path d="M12 2a7 7 0 0 0-7 7c0 5 7 13 7 13s7-8 7-13a7 7 0 0 0-7-7zm0 9.5A2.5 2.5 0 1 1 12 6.5a2.5 2.5 0 0 1 0 5z" fill="var(--brand-blue)"/></svg>
      </span>
    </div>
    <p class="contact__address">PO Box 48, Lindenweg 7<br>Harbour Lane Rivermark</p>
  </div>

  <p class="web">www.corvano-maler.com</p>
</section>

<section class="card card--back" aria-label="Business card back">
  <div class="brand">
    <div class="brand__row">
      <span class="brand__name">Corvano</span>
      <span class="brand__dot"></span>
    </div>
    <span class="brand__tag">Malerbetrieb</span>
  </div>
</section>

</body>
</html>
```